Natural Organic soap need packaging design

we need a packaging design for new company based in New Zealand Called 'Bremta Global ltd'.. We manufacture Natural organic soap bars.our main USP is that this soap is made of all natural ingredient and no chemical used and soap is made in New Zealand,so we need a design which look natural,simple,classy and luxury and packaging should reflect that its made in New Zealand.please find attached photos of sample soap.
soap will be in two variant:
1. Pure Manuka Honey soap
2. Goat Milk soap
NOTE: the soap in picture is not actually our soap its just a sample what our soap will look like so please don't make a design with KLOMPP written on it. BREMTA is the soap name.
Target Market(s)
international market. mainly young and kids
Industry/Entity Type
It Company

```html
<!DOCTYPE html>
<html lang="en">
<head>
<meta charset="utf-8">
<title>Bremta – Pure Manuka Honey Soap packaging</title>
<link href="https://fonts.googleapis.com/css2?family=Open+Sans:wght@400;600&display=swap" rel="stylesheet">
<style>
  :root {
    --backdrop: #dcdcdc;
    --carton-yellow: #e3a91b;
    --carton-yellow-deep: #d89d12;
    --label-red: #7e1317;
    --label-frame: #f3ead8;
    --honeycomb-red: #8f2027;
    --honeycomb-gold: #cf9420;
    --ink-light: #f4f0ea;
    --logo-silver: #d6d6d6;
  }
  * { margin: 0; padding: 0; box-sizing: border-box; }
  html, body {
    width: 1200px; height: 801px; overflow: hidden;
    background: var(--backdrop);
    font-family: "Open Sans", Arial, sans-serif;
  }
  .carton {
    position: absolute; left: 175px; top: 110px;
    width: 850px; height: 560px;
  }
  .carton-lid {
    position: absolute; left: 150px; top: 0;
    width: 700px; height: 370px;
    background: var(--carton-yellow);
  }
  .label-frame { position: absolute; left: 30px; top: 30px; width: 640px; height: 310px; }
  .honeycomb-lid {
    position: absolute; left: 380px; top: 170px; width: 220px; height: 130px;
    background: var(--honeycomb-red); border-radius: 14px; opacity: .6;
  }
  .label-content {
    position: absolute; left: 30px; top: 30px; width: 640px; height: 310px;
    display: flex; flex-direction: column; align-items: center; justify-content: center;
    color: var(--ink-light);
  }
  .product-name { font-size: 28px; font-weight: 400; letter-spacing: .3px; line-height: 1.2; }
  .label-content .product-name { margin-bottom: 12px; }
  .brand-name {
    font-size: 84px; font-weight: 600; letter-spacing: 6px;
    color: var(--logo-silver); line-height: 1;
  }
  .brand-origin {
    font-size: 13px; letter-spacing: 12px; color: var(--logo-silver);
    margin-top: 12px; font-weight: 600;
  }
  .carton-front {
    position: absolute; left: 150px; top: 370px;
    width: 700px; height: 190px;
    background: var(--carton-yellow-deep);
    display: flex; align-items: center; justify-content: space-between;
    padding: 0 60px;
  }
  .front-brand { color: var(--ink-light); text-align: center; }
  .front-brand .brand-name { font-size: 60px; color: var(--ink-light); letter-spacing: 4px; }
  .front-brand .brand-origin { color: var(--ink-light); opacity: .8; font-size: 10px; letter-spacing: 9px; margin-top: 8px; }
  .front-product { position: relative; display: flex; align-items: center; }
  .honeycomb-front {
    position: absolute; left: -40px; top: -20px; width: 150px; height: 110px;
    background: var(--honeycomb-gold); border-radius: 12px;
  }
  .front-product .product-name { position: relative; font-size: 28px; color: var(--ink-light); margin-left: 40px; }
  .carton-end {
    position: absolute; left: 0; top: 370px;
    width: 150px; height: 190px;
    background: var(--carton-yellow);
    border-right: 1px solid var(--carton-yellow-deep);
    display: flex; flex-direction: row-reverse; align-items: center; justify-content: center;
    gap: 8px; color: var(--ink-light);
  }
  .carton-end > * { writing-mode: vertical-rl; }
  .carton-end .product-name { font-size: 14px; }
  .carton-end .brand-name { font-size: 30px; letter-spacing: 2px; color: var(--ink-light); }
  .carton-end .brand-origin { font-size: 7px; letter-spacing: 5px; margin: 0; color: var(--ink-light); opacity: .8; }
</style>
</head>
<body>
  <main class="carton">
    <section class="carton-lid">
      <svg class="label-frame" viewBox="0 0 640 310" aria-hidden="true">
        <path d="M20 0 H620 A20 20 0 0 0 640 20 V290 A20 20 0 0 0 620 310 H20 A20 20 0 0 0 0 290 V20 A20 20 0 0 0 20 0 Z" fill="var(--label-red)"/>
        <path d="M26 8 H614 A18 18 0 0 0 632 26 V284 A18 18 0 0 0 614 302 H26 A18 18 0 0 0 8 284 V26 A18 18 0 0 0 26 8 Z" fill="none" stroke="var(--label-frame)" stroke-width="2"/>
      </svg>
      <div class="honeycomb-lid" role="img" aria-label="Faint honeycomb pattern decoration"></div>
      <div class="label-content">
        <p class="product-name">Pure Manuka Honey Soap</p>
        <h1 class="brand-name">BREMTA</h1>
        <p class="brand-origin">NEW ZEALAND</p>
      </div>
    </section>
    <section class="carton-end">
      <p class="product-name">Pure Manuka Honey Soap</p>
      <p class="brand-name">BREMTA</p>
      <p class="brand-origin">NEW ZEALAND</p>
    </section>
    <section class="carton-front">
      <div class="front-brand">
        <p class="brand-name">BREMTA</p>
        <p class="brand-origin">NEW ZEALAND</p>
      </div>
      <div class="front-product">
        <div class="honeycomb-front" role="img" aria-label="Honeycomb pattern decoration"></div>
        <p class="product-name">Pure Manuka<br>Honey Soap</p>
      </div>
    </section>
  </main>
</body>
</html>
```